Frostvale Cool Packs needs stationery designed for their new logo

We have a new logo so now want all our stationery to be redesigned.
Frostvale is a gel ice pack product used by the seafood & food industry to transport chilled products around the world.

We would like to use our new logo with icy or snow backgrounds or elements.
Our company tag line is "Keep your products chilled for longer"
I'll attach our old business cards so that you can use the text off them.
2nd attachment is our new logo to be used.

We want a design for:
- Business cards
- Letter Head
- Email signature

Target Market(s)

seafood & chilled food distributors

Industry/Entity Type

Industry

Font styles to use
Sans Serif

Colors
0492cd
85cae6
cee9f5

Requirements
Must have
• Our logo
Nice to have
• Snow or ice background or image incorporated somehow

```html
<!DOCTYPE html>
<html lang="en">
<head>
<meta charset="utf-8">
<title>Frostvale Cool Packs – Letterhead</title>
<link rel="stylesheet" href="https://fonts.googleapis.com/css2?family=Jost:ital,wght@0,400;0,600;0,700;1,400&family=Tinos&display=swap">
<style>
  :root {
    --brand-blue: #0492cd;
    --brand-cyan: #1fb8ea;
    --brand-aqua: #85cae6;
    --brand-ice: #cee9f5;
    --brand-navy: #2b3a8f;
    --paper-white: #ffffff;
    --body-ink: #111111;
    --backdrop: #eef2f5;
  }
  * { box-sizing: border-box; margin: 0; padding: 0; }
  html, body {
    width: 1200px; height: 1200px; overflow: hidden;
    background: var(--backdrop);
  }
  .letterhead {
    position: absolute; left: 190px; top: 20px;
    width: 820px; height: 1160px;
    background: radial-gradient(ellipse at 50% 45%, var(--paper-white) 35%, var(--brand-ice) 100%);
    box-shadow: 0 2px 10px rgba(0,0,0,0.12);
    overflow: hidden;
  }
  .letterhead__bands { position: absolute; inset: 0; width: 100%; height: 100%; }
  .tagline {
    position: absolute; right: 71px; top: 21px;
    font-family: "Jost", sans-serif; font-weight: 600;
    font-size: 19px; letter-spacing: 0.3px;
    color: var(--brand-navy); text-transform: uppercase;
  }
  .brand {
    position: absolute; left: 22px; top: 110px;
    display: flex; align-items: center; gap: 10px;
  }
  .brand__dot {
    width: 22px; height: 22px; border-radius: 50%;
    background: var(--paper-white);
  }
  .brand__name {
    font-family: "Jost", sans-serif; font-weight: 700;
    font-size: 38px; color: var(--paper-white); line-height: 1;
  }
  .letter {
    position: absolute; left: 111px; top: 302px; width: 630px;
    font-family: "Tinos", serif; font-size: 16px; line-height: 20px;
    color: var(--body-ink);
  }
  .letter p { margin-bottom: 20px; }
  .signatory {
    position: absolute; right: 18px; top: 980px; text-align: right;
    font-family: "Jost", sans-serif; color: var(--paper-white);
  }
  .signatory__name { font-weight: 600; font-size: 27px; line-height: 34px; }
  .signatory__role { font-style: italic; font-size: 17px; line-height: 22px; margin-right: 8px; }
  .contact {
    position: absolute; left: 455px; top: 1108px;
    font-family: "Jost", sans-serif; color: var(--brand-navy);
  }
  .contact__row { display: flex; align-items: center; gap: 8px; height: 25px; }
  .contact__row--email { font-size: 16px; }
  .contact__row--web { font-size: 17px; font-weight: 600; letter-spacing: 1px; }
  .contact__icon { width: 16px; height: 16px; flex: none; }
</style>
</head>
<body>
  <main class="letterhead">
    <svg class="letterhead__bands" viewBox="0 0 932 1318" preserveAspectRatio="none" aria-hidden="false">
      <defs>
        <linearGradient id="bandCyan" x1="0" y1="0" x2="1" y2="0">
          <stop offset="0" stop-color="#1fb8ea"/>
          <stop offset="0.5" stop-color="#8fd0dd"/>
          <stop offset="1" stop-color="#1fb8ea"/>
        </linearGradient>
        <linearGradient id="bandIce" x1="0" y1="0" x2="1" y2="1">
          <stop offset="0" stop-color="#bfe0f0"/>
          <stop offset="0.5" stop-color="#e6f3fa"/>
          <stop offset="1" stop-color="#a9d6ec"/>
        </linearGradient>
      </defs>
      <g class="header-band">
        <path d="M0,0 Q470,110 932,30 L932,60 Q600,240 0,205 Z" fill="url(#bandCyan)"/>
        <path role="img" aria-label="Frosted ice texture band" d="M0,205 Q600,240 932,60 L932,115 Q560,228 0,270 Z" fill="url(#bandIce)"/>
      </g>
      <g class="footer-band">
        <path role="img" aria-label="Frosted ice texture band" d="M0,1265 Q420,1050 932,1012 L932,1075 Q500,1070 0,1300 Z" fill="url(#bandIce)"/>
        <path d="M0,1300 Q500,1070 932,1075 L932,1275 Q470,1160 0,1310 Z" fill="url(#bandCyan)"/>
      </g>
    </svg>

    <div class="tagline">Keep your products chilled for longer</div>

    <div class="brand">
      <span class="brand__dot"></span>
      <span class="brand__name">Frostvale</span>
    </div>

    <article class="letter">
      <p>Date</p>
      <p>Dear Credit Union Member:</p>
      <p>On March 20, 2009, the Federal Mutual Savings Board (FMSB), the federal regulator for federally insured credit unions, placed two “corporate credit unions”—Central Summit Federal Credit Union and Pacific Corporate (Pacorp) Federal Credit Union into conservatorship. “Corporate credit unions are similar to Federal Reserve Banks and do not deal directly with consumers, but provide investment, financing, check clearing and other services to “retail credit unions” (also called natural person credit unions) such as your _______ Credit Union.</p>
      <p>We wish to assure you that these actions by FMSB have nothing whatsoever to do with ______ Credit Union and do not affect your deposits at ________ Credit Union. In fact, FMSB’s actions to stabilize corporate credit unions were taken to assure the continued safety and soundness of local “retail” credit unions. You can rest assured that your funds on deposit are insured by the Mutual Savings Share Insurance Fund (MSSIF) and continue to be backed by the full faith and credit of the United States Government, up to at least $250,000. In addition, Individual Retirement Accounts (IRAs) are insured separately up to $250,000.</p>
      <p>While “retail” credit unions have not been immune to the national economic downturn, we are well capitalized overall, we are strong, and we are well-positioned to weather the current turbulence affecting our nation’s economy.</p>
      <p>We thank you for your continued participation as a member of your credit union. Please do not hesitate to contact us here at your credit union if you have any concerns or questions.</p>
      <p>Sincerely,</p>
    </article>

    <div class="signatory">
      <div class="signatory__name">Marcus Hale</div>
      <div class="signatory__role">Business Development</div>
    </div>

    <div class="contact">
      <div class="contact__row contact__row--email">
        <svg class="contact__icon" viewBox="0 0 16 16" aria-hidden="true">
          <rect x="1" y="3" width="14" height="10" fill="none" stroke="currentColor" stroke-width="1.6"/>
          <path d="M1,3 L8,9 L15,3" fill="none" stroke="currentColor" stroke-width="1.6"/>
        </svg>
        <span>marcus.hale@frostvale.com.au</span>
      </div>
      <div class="contact__row contact__row--web">
        <svg class="contact__icon" viewBox="0 0 16 16" aria-hidden="true">
          <circle cx="8" cy="8" r="6.5" fill="none" stroke="currentColor" stroke-width="1.6"/>
          <ellipse cx="8" cy="8" rx="2.8" ry="6.5" fill="none" stroke="currentColor" stroke-width="1.2"/>
          <path d="M1.5,8 H14.5" stroke="currentColor" stroke-width="1.2"/>
        </svg>
        <span>www.frostvale.com.au</span>
      </div>
    </div>
  </main>
</body>
</html>
```